Bref créative
Brochure for a Peforming Arts Private School
Whitford Lane
Institute of Global Learning, Creative and Stage Crafts
Vision:
Whitford Lane Academy will engage and enrich students using the fine arts and a rigorous curriculum so that they are prepared for life after school. Through the fine arts, students become more successful and experience the world in a more holistic manner. Through rigorous curriculum, students are prepared for professional opportunities. Students will focus their passion for music, theater, art, dance, and international studies.
I will upload the school's prospectus to provide other details that might be important to add.
Education
The target audience is more for Corporate and Parent meetings, so that the company can introduce itself and the audience can have something to take with them.
I would like the brochure to have the following:
1. Color
2. Professional Look
3. School Logo
4. Information about the school - including vision, majors, course types, etc.
4. Non-discrimanatory policy - written in smaller print at the bottom of the back of the brochure
5. Visuals to represent the ideas of theater, dance, art, music, and international studies.
Please use the first paragraph.

```html
<!DOCTYPE html>
<html lang="en">
<head>
<meta charset="utf-8">
<title>Whitford Lane Academy Brochure</title>
<link rel="stylesheet" href="https://fonts.googleapis.com/css2?family=Cinzel:wght@400;700&family=Open+Sans:wght@400;600;700&display=swap">
<style>
  :root {
    --page-bg: #ece7df;
    --paper: #ffffff;
    --navy: #262b4a;
    --navy-deep: #1c2038;
    --gold: #d6b35a;
    --brown: #7a4a2c;
    --brown-light: #a7765a;
    --tan: #efe4d6;
    --tan-row: #f6eee3;
    --plum: #5b3e6e;
    --ink: #333333;
    --ink-soft: #666666;
    --rule: #c9b9a6;
    --photo-a: #7c5b45;
    --photo-b: #c39a72;
  }
  * { box-sizing: border-box; margin: 0; padding: 0; }
  html, body { width: 1200px; height: 515px; overflow: hidden; }
  body {
    background: var(--page-bg);
    font-family: "Open Sans", Arial, sans-serif;
    color: var(--ink);
    position: relative;
  }
  .spread {
    position: absolute;
    top: 36px;
    height: 444px;
    background: var(--paper);
    display: flex;
    overflow: hidden;
    box-shadow: 0 2px 6px rgba(0,0,0,0.18);
  }
  .spread--outside { left: 24px; width: 552px; }
  .spread--inside { left: 612px; width: 576px; }
  .panel {
    flex: 1;
    padding: 12px 12px;
    overflow: hidden;
    position: relative;
    font-size: 5.6px;
    line-height: 1.5;
  }
  .panel + .panel { border-left: 1px solid #e6e0d8; }
  .panel h2 {
    font-size: 7px;
    font-weight: 700;
    color: var(--navy);
    margin-bottom: 4px;
  }
  .panel p { margin-bottom: 6px; color: var(--ink); }
  .fine { font-size: 4.4px; color: var(--ink-soft); line-height: 1.45; }

  /* intake table */
  .grid-table { width: 100%; border-collapse: collapse; margin: 6px 0 8px; font-size: 5px; }
  .grid-table th {
    background: var(--navy);
    color: var(--paper);
    font-weight: 600;
    padding: 2px 4px;
    text-align: left;
  }
  .grid-table td { padding: 1.5px 4px; border-bottom: 1px solid #e5e1dc; }
  .grid-table tr:nth-child(even) td { background: var(--tan-row); }

  /* contact */
  .contact {
    position: absolute;
    left: 12px; right: 12px; bottom: 14px;
    text-align: center;
    font-size: 5.4px;
    color: var(--ink);
  }
  .contact .contact-name { font-weight: 700; margin-bottom: 4px; }
  .contact-line { display: flex; align-items: center; justify-content: center; gap: 3px; }

  /* cover */
  .cover {
    background: var(--navy);
    color: var(--paper);
    display: flex;
    flex-direction: column;
    align-items: center;
    padding-top: 58px;
  }
  .cover-title {
    font-family: "Cinzel", Georgia, serif;
    color: var(--gold);
    font-size: 20px;
    font-weight: 400;
    text-align: center;
    line-height: 1.2;
  }
  .brand-mark {
    margin-top: 46px;
    display: flex;
    flex-direction: column;
    align-items: center;
    gap: 8px;
  }
  .brand-mark .dot {
    width: 60px; height: 60px; border-radius: 50%;
    background: var(--gold);
  }
  .brand-mark .name {
    font-family: "Cinzel", Georgia, serif;
    color: var(--gold);
    font-size: 8px;
  }
  .cover-url {
    position: absolute; bottom: 16px; left: 0; right: 0;
    text-align: center; font-size: 5.4px; color: #c8cbe0;
  }

  /* inside */
  .spread--inside { flex-direction: column; }
  .inside-bar { height: 6px; background: var(--brown); flex: none; }
  .inside-body { display: flex; flex: 1; }
  .edge-strip { width: 8px; background: var(--brown-light); flex: none; }
  .section-label {
    font-size: 7.5px; font-weight: 700; color: var(--brown);
    border-bottom: 1px solid var(--rule); padding-bottom: 2px; margin-bottom: 5px;
  }
  .photo {
    height: 118px;
    margin: 0 -12px 8px;
    background: linear-gradient(135deg, var(--photo-a), var(--photo-b));
  }
  .pillars { display: flex; gap: 4px; justify-content: center; margin: 8px 0 10px; }
  .pillar {
    color: var(--paper); font-size: 6px; font-weight: 600;
    padding: 4px 8px; border-radius: 2px;
  }
  .pillar--inspire { background: var(--brown); }
  .pillar--create { background: var(--navy); }
  .pillar--excel { background: var(--plum); }
  .mission-brand {
    position: absolute; bottom: 14px; left: 0; right: 0;
    display: flex; align-items: center; justify-content: center; gap: 5px;
  }
  .mission-brand .dot { width: 22px; height: 22px; border-radius: 50%; background: var(--navy); }
  .mission-brand .name { font-family: "Cinzel", Georgia, serif; font-size: 7px; color: var(--navy); }

  .majors-table { width: 100%; border-collapse: collapse; font-size: 5px; margin-top: 4px; }
  .majors-table th {
    background: var(--brown); color: var(--paper);
    text-align: left; padding: 2px 4px; font-weight: 600;
  }
  .majors-table td { padding: 2px 4px; border-bottom: 1px solid #ece4d8; vertical-align: top; }
  .majors-table tr:nth-child(odd) td { background: var(--tan); }

  .course-title { font-size: 6px; font-weight: 700; color: var(--brown); margin: 6px 0 3px; text-transform: uppercase; }
  .course-table { width: 100%; border-collapse: collapse; font-size: 4.8px; }
  .course-table th { text-align: left; color: var(--navy); font-weight: 700; padding: 1.5px 3px; border-bottom: 1px solid var(--rule); }
  .course-table td { padding: 1.2px 3px; }
  .course-table tr:nth-child(even) td { background: var(--tan-row); }
</style>
</head>
<body>

<!-- Outside spread -->
<section class="spread spread--outside">
  <div class="panel intake">
    <h2>Intake</h2>
    <p>Whitford Lane Academy accepts students entering grades six through twelve. Places are offered after a short interview, a review of school records and an audition or portfolio in the chosen major.</p>
    <table class="grid-table">
      <tr><th>Course</th><th>Round</th></tr>
      <tr><td>Music</td><td>Autumn</td></tr>
      <tr><td>Theater</td><td>Autumn</td></tr>
      <tr><td>Dance</td><td>Winter</td></tr>
      <tr><td>Visual Art</td><td>Winter</td></tr>
      <tr><td>Global Studies</td><td>Spring</td></tr>
    </table>
    <p>Students will have the opportunity to visit classes, meet faculty and attend a showcase before they decide. Families are welcome to book a campus tour at any time during the school year.</p>
    <p>Tuition support is available for qualifying families. Please ask the admissions office for the application pack and current deadlines.</p>
    <p class="fine">Whitford Lane Academy admits students of any race, colour, religion, national and ethnic origin to all the rights, privileges, programs and activities generally made available to students at the school. It does not discriminate on the basis of race, colour, religion, national and ethnic origin in the administration of its educational policies, admissions policies, scholarship programs, and athletic and other school administered programs.</p>
  </div>

  <div class="panel about">
    <h2>Student Life</h2>
    <p>Students spend the morning on a rigorous academic program and the afternoon in studios, rehearsal rooms and workshops led by working artists. Small classes let every student be known by name.</p>
    <p>Each year ends with a festival of concerts, plays, dance recitals and exhibitions open to families and the wider community. Students also take part in exchange trips and global study projects.</p>
    <p>Our Community Association of families, staff and partners supports events, scholarships and new facilities so that every student can grow with confidence.</p>
    <div class="contact">
      <div class="contact-name">Whitford Lane Academy</div>
      <div class="contact-line">
        <svg width="6" height="6" viewBox="0 0 10 10" aria-hidden="true"><path d="M2 1l2 2-1 1.5c.8 1.4 1.6 2.2 3 3L7.5 6l2 2-1.5 1.5C4.5 9 1 5.5.5 2z" fill="#262b4a"/></svg>
        <span>(555) 014-2207</span>
      </div>
      <div class="contact-line">
        <svg width="6" height="6" viewBox="0 0 10 10" aria-hidden="true"><path d="M5 0a3.5 3.5 0 0 0-3.5 3.5C1.5 6 5 10 5 10s3.5-4 3.5-6.5A3.5 3.5 0 0 0 5 0zm0 5a1.5 1.5 0 1 1 0-3 1.5 1.5 0 0 1 0 3z" fill="#262b4a"/></svg>
        <span>48 Orchard Row, Fairmont</span>
      </div>
      <div class="contact-line"><span>info@whitfordlane.example</span></div>
    </div>
  </div>

  <div class="panel cover">
    <h1 class="cover-title">Whitford Lane<br>Academy</h1>
    <div class="brand-mark">
      <div class="dot"></div>
      <div class="name">Whitford Lane</div>
    </div>
    <div class="cover-url">www.whitfordlane.example</div>
  </div>
</section>

<!-- Inside spread -->
<section class="spread spread--inside">
  <div class="inside-bar"></div>
  <div class="inside-body">
    <div class="panel mission">
      <div class="section-label">Mission</div>
      <div class="photo" role="img" aria-label="Photo of students performing on stage"></div>
      <p>Whitford Lane Academy will engage and enrich students using the fine arts and a rigorous curriculum so that they are prepared for life after school. Through the fine arts, students become more successful and experience the world in a more holistic manner.</p>
      <div class="pillars">
        <span class="pillar pillar--inspire">Inspire</span>
        <span class="pillar pillar--create">Create</span>
        <span class="pillar pillar--excel">Excel</span>
      </div>
      <p>Through rigorous curriculum, students are prepared for professional opportunities. Students will focus their passion for music, theater, art, dance, and international studies.</p>
      <div class="mission-brand">
        <div class="dot"></div>
        <div class="name">Whitford Lane Academy</div>
      </div>
    </div>

    <div class="panel majors">
      <div class="section-label">Majors</div>
      <p>Students will begin their chosen major program within the ninth grade. Each major blends studio time, performance and academic study, with the support of faculty mentors.</p>
      <p>Students may change major once after a review with their advisor and the department head.</p>
      <table class="majors-table">
        <tr><th>Major</th><th>Focus</th></tr>
        <tr><td>Music</td><td>Voice, strings, winds, composition</td></tr>
        <tr><td>Theater</td><td>Acting, directing, stagecraft</td></tr>
        <tr><td>Dance</td><td>Ballet, modern, jazz, choreography</td></tr>
        <tr><td>Visual Art</td><td>Drawing, painting, sculpture, design</td></tr>
        <tr><td>Global Studies</td><td>Languages, culture, world affairs</td></tr>
        <tr><td>Media Arts</td><td>Film, sound, digital production</td></tr>
        <tr><td>Creative Writing</td><td>Poetry, fiction, scriptwriting</td></tr>
        <tr><td>Stage Design</td><td>Lighting, sets, costume</td></tr>
      </table>
    </div>

    <div class="panel curriculum">
      <div class="section-label">Curriculum</div>
      <p>The following pages list the standard academic courses each student completes alongside the chosen major.</p>
      <div class="course-title">Subject Course Types</div>
      <table class="course-table">
        <tr><th>English</th><th>Honors</th></tr>
        <tr><td>English I</td><td>English I H</td></tr>
        <tr><td>English II</td><td>English II H</td></tr>
        <tr><td>English III</td><td>AP Language</td></tr>
        <tr><td>English IV</td><td>AP Literature</td></tr>
        <tr><th>Math</th><th>Honors</th></tr>
        <tr><td>Algebra I</td><td>Algebra I H</td></tr>
        <tr><td>Geometry</td><td>Geometry H</td></tr>
        <tr><td>Algebra II</td><td>Pre-Calculus H</td></tr>
        <tr><td>Statistics</td><td>AP Calculus</td></tr>
        <tr><th>Science</th><th>Honors</th></tr>
        <tr><td>Biology</td><td>Biology H</td></tr>
        <tr><td>Chemistry</td><td>Chemistry H</td></tr>
        <tr><td>Physics</td><td>AP Physics</td></tr>
        <tr><th>Social Studies</th><th>Honors</th></tr>
        <tr><td>World History</td><td>AP World</td></tr>
        <tr><td>Civics</td><td>AP Government</td></tr>
        <tr><td>Economics</td><td>AP Economics</td></tr>
      </table>
    </div>
    <div class="edge-strip"></div>
  </div>
</section>

</body>
</html>
```